Verpackungen für ein Mundgel
Zielgruppe
Hallo Zusammen :-)
Wir sind eine kleine Vertriebsfirma und bringen ein neues innovatives Mundgel auf den Markt. Unsere Zielgruppen sind alle Personen mit Probleme im Mundraum (Aphthen, Zahnfleischentzündungen, Druckstellen...etc.).
Aufgabenstellung
Die Verpackung wird für ein neues Mundgel benötigt. Die Stanzvorlage ist mit angehängt. Wichtig ist, dass die Gestaltung vertikal angebracht wird. Das Produkt ist 100% rein natürlich (komplett ohne Chemie).
Vom Design her soll die Kernbotschaft (innovative Einwirkformel für das Zahnfleisch & 100% Kräuterhain & Manuka Honig (ein Inhaltsstoff)) wiedergespiegelt werden. Es kann gerne ein modernes 'medizinisches' Design sein.
Der Produktname lautet 'Velisa Mundgel'. Es geht erstmal nur um das Design. Die Pflichttexte...etc. werden dem Gewinner später bekannt gegeben und können im Nachhinein noch auf die Verpackung mit angebracht werden.
Wir freuen uns schon jetzt auf Eure kreativen Vorschläge :-)

```html
<!DOCTYPE html>
<html lang="de">
<head>
<meta charset="utf-8">
<title>Velisa Mundgel – Verpackung</title>
<link rel="stylesheet" href="https://fonts.googleapis.com/css2?family=Jost:wght@300;400&family=Signika:wght@700&display=swap">
<style>
  :root {
    --stage: #eef0ea;
    --panel: #ffffff;
    --green: #5b9a4e;
    --badge-green: #62a735;
    --logo-green: #3d8b3f;
    --ink: #3a3a3a;
    --leaf-soft: #cfe3a8;
    --leaf-light: #eef5dd;
    --honey: #f1e35a;
  }
  html, body {
    margin: 0;
    width: 1200px;
    height: 705px;
    overflow: hidden;
    background: var(--stage);
  }
  .pack-front {
    position: absolute;
    left: 40px;
    top: 198px;
    width: 1120px;
    height: 308px;
    background: var(--panel);
    overflow: hidden;
    box-shadow: 0 2px 10px rgba(0,0,0,0.12);
  }
  .flow-left {
    position: absolute;
    left: 0; top: 0;
    width: 405px; height: 308px;
    background:
      radial-gradient(ellipse 150px 120px at 205px 150px, #fff 55%, rgba(255,255,255,0) 100%),
      radial-gradient(ellipse 220px 160px at 40px 300px, var(--honey) 0%, rgba(241,227,90,0) 75%),
      linear-gradient(160deg, #a6c763 0%, var(--leaf-soft) 25%, var(--leaf-light) 55%, #fff 100%);
  }
  .flow-right {
    position: absolute;
    right: 0; bottom: 0;
    width: 300px; height: 260px;
    background: radial-gradient(ellipse 260px 200px at 320px 240px, var(--leaf-soft) 0%, var(--leaf-light) 45%, rgba(255,255,255,0) 80%);
  }
  .brand-mark {
    position: absolute;
    left: 72px;
    top: 130px;
    display: flex;
    align-items: center;
    gap: 10px;
    font-family: "Jost", sans-serif;
    font-weight: 400;
    font-size: 30px;
    letter-spacing: 2px;
    color: var(--logo-green);
  }
  .brand-dot {
    width: 22px; height: 22px;
    border-radius: 50%;
    background: var(--logo-green);
  }
  .formula-badge {
    position: absolute;
    right: 0; top: 0;
    width: 409px; height: 56px;
    background: var(--badge-green);
    color: #fff;
    font-family: "Signika", sans-serif;
    font-weight: 700;
    font-size: 20px;
    letter-spacing: 3px;
    display: flex;
    align-items: center;
    justify-content: center;
  }
  .product-line {
    position: absolute;
    left: 488px; top: 78px;
    width: 288px;
    margin: 0;
    text-align: center;
    font-family: "Jost", sans-serif;
    font-weight: 300;
    font-size: 57px;
    line-height: 1;
    letter-spacing: 9px;
    color: var(--ink);
  }
  .product-name {
    position: absolute;
    left: 380px; top: 135px;
    width: 506px;
    margin: 0;
    text-align: center;
    font-family: "Jost", sans-serif;
    font-weight: 400;
    font-size: 92px;
    line-height: 1;
    letter-spacing: 8px;
    color: var(--green);
  }
  .tagline {
    position: absolute;
    left: 300px; top: 224px;
    width: 662px;
    margin: 0;
    text-align: center;
    font-family: "Jost", sans-serif;
    font-weight: 300;
    font-size: 15px;
    letter-spacing: 1px;
    color: var(--ink);
    white-space: nowrap;
  }
  .tagline strong {
    font-family: "Signika", sans-serif;
    font-weight: 700;
    color: var(--green);
  }
</style>
</head>
<body>
  <main class="pack-front">
    <div class="flow-left" role="img" aria-label="Weiche grün-gelbe Schwünge als Hintergrund"></div>
    <div class="flow-right" role="img" aria-label="Weiche grüne Schwünge in der Ecke"></div>
    <div class="brand-mark"><span class="brand-dot"></span>Kräuterhain</div>
    <div class="formula-badge">MIT NEUER INNOVATIVER FORMEL</div>
    <p class="product-line">VELISA</p>
    <h1 class="product-name">MUNDGEL</h1>
    <p class="tagline">REIN NATÜRLICHES GEL MIT <strong>MANUKA-HONIG</strong> ZUR ANWENDUNG IN DER MUNDHÖHLE</p>
  </main>
</body>
</html>
```